We need a fresh, new church business card!!

We need a church business card with basic info to hand out as invites. We are looking for something clean that communicates our basic information clearly.

We are open to square or rectangle card sizes.

General Public

Religious

The attached logo is the only one that I have available. We'd like to see options with with text of the logo lighter and on a dark background as well as options with white/light backgrounds.

Also, we'd like to see option with rounded corners.

• Address - 2718 Maple Row, Rockford, IL 61142
• Website - brookvane.example
• Phone - 815-555-0163
• Service times -
• Sunday - 10am Sunday School
• - 11am Family Worship
• - 6pm Night of Prayer
• Wednesday - 7:30pm Adult Bible Study
• Classes for all ages

```html
<!DOCTYPE html>
<html lang="en">
<head>
<meta charset="utf-8">
<title>Brookvane Pentecostal Church – Business Cards</title>
<link href="https://fonts.googleapis.com/css2?family=EB+Garamond:wght@400;600&display=swap" rel="stylesheet">
<style>
  :root {
    --stage: #1c1c1c;
    --card-dark: #6a6a6a;
    --card-grey: #6f6f6f;
    --card-white: #f7f7f7;
    --teal: #3f8594;
    --text-light: #e6e6e6;
    --text-soft: #cfcfcf;
    --brand-dark: #4a4a4a;
  }
  * { margin: 0; padding: 0; box-sizing: border-box; }
  html, body { width: 1200px; height: 873px; overflow: hidden; background: var(--stage); }
  body { position: relative; font-family: "EB Garamond", Georgia, serif; }

  .card {
    position: absolute;
    width: 540px;
    height: 309px;
    border-radius: 6px;
    overflow: hidden;
  }

  /* Back of card: dark with light name */
  .card--back { left: 40px; top: 282px; background: var(--card-dark); }
  .card--back .brand {
    position: absolute; left: 0; right: 0; top: 110px;
    display: flex; align-items: center; justify-content: center; gap: 16px;
    color: var(--text-light);
  }
  .card--back .website {
    position: absolute; left: 0; right: 0; top: 205px;
    text-align: center; color: var(--text-soft);
    font-size: 15px; letter-spacing: 2px;
  }

  .brand-dot { width: 44px; height: 44px; border-radius: 50%; flex: none; }
  .card--back .brand-dot { background: var(--text-light); }
  .card--front .brand-dot { background: var(--teal); }
  .brand-name { font-weight: 400; font-size: 30px; line-height: 1; letter-spacing: 1px; }
  .brand-name small { display: block; font-size: 14px; letter-spacing: 4px; margin-top: 4px; }

  /* Front of card: light top, wave, grey info panel */
  .card--front { left: 620px; top: 282px; background: var(--card-grey); }
  .card--front .wave { position: absolute; inset: 0; }
  .card--front .brand {
    position: absolute; left: 100px; top: 42px;
    display: flex; align-items: center; gap: 14px;
    color: var(--brand-dark);
  }

  .service-times {
    position: absolute; left: 26px; top: 188px;
    color: var(--text-soft); font-size: 13.5px; line-height: 1.3;
  }
  .service-times h2 {
    font-size: 16px; font-weight: 600; color: var(--text-light);
    text-decoration: underline; text-underline-offset: 2px; margin-bottom: 1px;
  }
  .service-times b { font-weight: 600; color: var(--text-light); }
  .service-times .all-ages { font-size: 15px; color: var(--text-light); margin-top: 4px; letter-spacing: .5px; }

  .contact {
    position: absolute; left: 300px; top: 170px;
    list-style: none; color: var(--text-soft); font-size: 13.5px;
  }
  .contact li { display: flex; align-items: center; gap: 10px; margin-bottom: 10px; }
  .contact svg { width: 14px; height: 14px; flex: none; }
</style>
</head>
<body>

  <section class="card card--back" aria-label="Card back">
    <div class="brand">
      <span class="brand-dot"></span>
      <div class="brand-name">BROOKVANE<small>PENTECOSTAL CHURCH</small></div>
    </div>
    <p class="website">www.brookvane.example</p>
  </section>

  <section class="card card--front" aria-label="Card front">
    <svg class="wave" viewBox="0 0 540 309" preserveAspectRatio="none" aria-hidden="true">
      <path d="M0 0 H540 V62 C470 120 330 160 0 185 V0 Z" fill="var(--teal)"/>
      <path d="M0 0 H540 V48 C470 108 330 148 0 170 V0 Z" fill="var(--card-white)"/>
    </svg>

    <div class="brand">
      <span class="brand-dot"></span>
      <div class="brand-name">BROOKVANE<small>PENTECOSTAL CHURCH</small></div>
    </div>

    <div class="service-times">
      <h2>SERVICE TIMES:</h2>
      <p>Sunday - 10:00am Sunday School</p>
      <p><b>11:00am:</b> Family Worship</p>
      <p><b>06:00pm:</b> Night of Prayer</p>
      <p>Wednesday - 7:30pm Adult Bible Study</p>
      <p class="all-ages">CLASSES FOR ALL AGES</p>
    </div>

    <ul class="contact">
      <li>
        <svg viewBox="0 0 14 14" aria-hidden="true"><rect x="3" y="0.5" width="8" height="13" rx="1.5" fill="none" stroke="var(--text-soft)"/><line x1="6" y1="11.5" x2="8" y2="11.5" stroke="var(--text-soft)"/></svg>
        815-555-0163
      </li>
      <li>
        <svg viewBox="0 0 14 14" aria-hidden="true"><rect x="0.5" y="2.5" width="13" height="9" fill="none" stroke="var(--text-soft)"/><path d="M0.5 2.5 L7 8 L13.5 2.5" fill="none" stroke="var(--text-soft)"/></svg>
        2718 Maple Row, Rockford, IL 61142
      </li>
    </ul>
  </section>

</body>
</html>
```